I am starting a company that will help small businesses that are looking to raise money over the internet (i.e. crowd fund) in reliance of the JOBS Act and the new rules that have been recently passed.

Initially, the website will help a business figure out if it is qualified to raise money and if so, it will tell the business what information is required.

The various pages will need to gather information from the businesses through Yes/No questionnaires, drop-down lists and free text boxes -

I am still thinking about my company's name and don't have a logo - for now, please use the name "RPMH (raise path mentor hub)" - feel free to throw in an idea for a logo

Hi all - I was wondering if I could get some design suggestions that don't use stock photos- thanks

Based on the designs I have received so far, I don't think the description of my website is clear.  The website will NOT be a crowdfunding portal (i.e. it is not like boostwell etc.)  It is an information website that will allow companies to determine if they are legally able to raise money online. 

If they are able to raise money online, then the company can sign-up for some paid services which include legal documents and agreements.

To help the design process, I've uploaded a draft of the questions that a company will need to answer to determine if it is able to raise money online.

The submitted designs should be for both the homepage as well as the pages on which the questions will be set out.

Thanks for taking the time to read.

small businesses that will be looking to raise money through crowd funding

Internet

• I need designs for the following pages:

1. Home page
- should be simple - links to 'about' page and 'blog' page
- room at the bottom for affiliate links/logos
- convey the message that there are many rules that need to be followed to legally crowd fund a company but that this website makes compliance easy
- prominent 'get started' button

2. Company questions pages
- laid out to ask ~ 5 questions:
- name of company (free text answer)
- amount raised in prior 12 months (drop down box)
- state of formation (drop down box)
- registered with the NRB (y/n)
- registered as an investment company (y/n)

- needs to be a help 'icon' beside the questions so that user can hover over the icon and get more information as to what the question is asking

3. Eligibility questions page
- list of ~25 questions (y/n) answers
-
4. Fund raising objectives page
- list of ~15 questions answers
- answers will be y/n, multiple choice, drop down menu or free text

5. Results page
- if company is not-eligible to proceed, display "Not Eligible" page with list of reasons why
- if company is eligible, display "Congratulations" page with link to "Sign-up and Continue"

6. Sign-up page
- name
- address
- e-mail etc.
- check box to agree to terms and conditions

7. 'blog' page

8. about / disclaimer page

```html
<!DOCTYPE html>
<html lang="en">
<head>
<meta charset="utf-8">
<title>RPMH – Crowdfunding Compliance for Businesses</title>
<link rel="stylesheet" href="https://fonts.googleapis.com/css2?family=Yanone+Kaffeesatz:wght@300;400;500&family=Open+Sans:ital,wght@0,400;0,700;1,400&display=swap">
<style>
  :root {
    --green: #7fcd1e;
    --green-dark: #5fa012;
    --nav-bg: #444444;
    --logo-bg: #2b2b2b;
    --text: #333333;
    --muted: #777777;
    --heading-grey: #666666;
    --track: #e2e2e4;
    --white: #ffffff;
  }
  * { box-sizing: border-box; margin: 0; padding: 0; }
  html, body { width: 1200px; height: 1031px; overflow: hidden; background: var(--white); }
  body { position: relative; font-family: "Open Sans", Arial, sans-serif; color: var(--text); }
  .abs { position: absolute; }

  /* top utility bar */
  .utility { top: 0; left: 0; width: 1200px; height: 34px; font-family: Arial, Helvetica, sans-serif; font-size: 12.5px; }
  .utility .phone { position: absolute; left: 757px; top: 9px; }
  .utility .divider { position: absolute; left: 862px; top: 7px; width: 1px; height: 20px; background: #c8c8c8; }
  .utility .account { position: absolute; left: 873px; top: 9px; }
  .utility .account a { color: var(--green); font-weight: bold; text-decoration: none; }

  /* navigation */
  .navbar { top: 34px; left: 0; width: 1200px; height: 62px; background: var(--nav-bg); }
  .brand { position: absolute; left: 105px; top: 0; width: 72px; height: 62px; background: var(--logo-bg); border-top: 3px solid var(--green);
    color: var(--white); font-family: "Yanone Kaffeesatz", sans-serif; font-size: 29px; font-weight: 400; text-align: center; line-height: 57px; letter-spacing: 0.5px; }
  .nav-link { position: absolute; top: 21px; color: var(--white); font-size: 14px; text-decoration: none; }
  .search { position: absolute; left: 847px; top: 14px; width: 238px; height: 35px; background: var(--white); border-radius: 3px; }
  .search span { position: absolute; left: 10px; top: 9px; font-size: 11px; font-style: italic; color: #888; }
  .search svg { position: absolute; right: 10px; top: 9px; }

  /* hero */
  .hero { top: 96px; left: 0; width: 1200px; height: 370px;
    background: linear-gradient(90deg, #b9c9a9 0%, #e7e6e2 18%, #f1f0ec 45%, #eceae5 70%, #d9d7d2 100%); }
  .hero-portrait { position: absolute; left: 90px; top: 0; width: 455px; height: 370px;
    background: linear-gradient(180deg, #c6a58f 0%, #d9c4b6 35%, #e6e6e6 60%, #efefef 100%); border-radius: 40% 40% 0 0 / 30% 30% 0 0; }
  .hero-title { position: absolute; left: 609px; top: 92px; font-family: "Yanone Kaffeesatz", sans-serif; font-weight: 500; font-size: 64px; line-height: 54px; letter-spacing: 1px; color: var(--green); }
  .hero-sub { position: absolute; left: 614px; top: 306px; font-size: 24px; line-height: 32px; font-weight: 400; color: #444; }
  .hero-sub { top: 306px; }
  .cta { position: absolute; left: 613px; top: 259px; width: 197px; height: 44px; background: var(--green); border-bottom: 3px solid var(--green-dark);
    color: var(--white); font-size: 14.5px; font-weight: 700; line-height: 42px; padding-left: 26px; text-decoration: none; }
  .cta svg { position: absolute; right: 22px; top: 15px; }

  /* section headings */
  .section-title { font-family: "Yanone Kaffeesatz", sans-serif; font-weight: 400; font-size: 38px; line-height: 44px; color: var(--green); }

  /* eligibility block */
  .feature-photo { left: 116px; top: 570px; width: 472px; height: 314px; background: linear-gradient(120deg, #e43a3a 0%, #d9c9a8 38%, #cfe0ee 70%, #b9c6d6 100%); }
  .feature-title { left: 610px; top: 565px; font-family: "Yanone Kaffeesatz", sans-serif; font-weight: 300; font-size: 33px; line-height: 40px; color: var(--heading-grey); }
  .feature-body { left: 610px; top: 612px; width: 480px; font-size: 14.3px; line-height: 22.7px; color: var(--muted); }
  .feature-link { left: 610px; top: 712px; font-family: "Yanone Kaffeesatz", sans-serif; font-size: 19px; line-height: 24px; font-style: italic; color: var(--green); text-decoration: none; }
  .progress { left: 608px; top: 802px; width: 351px; height: 15px; background: var(--track); border-radius: 3px; overflow: hidden; }
  .progress .fill { width: 225px; height: 100%; background: var(--green); }
  .stat-label { top: 833px; font-size: 14.5px; line-height: 18px; color: var(--muted); }
  .stat-value { top: 852px; font-family: "Yanone Kaffeesatz", sans-serif; font-weight: 400; font-size: 40px; line-height: 36px; color: var(--green); }
  .stat-value small { font-size: 24px; }

  /* blog thumbnails */
  .thumb { top: 1013px; width: 226px; height: 30px; }
</style>
</head>
<body>

<header class="abs utility">
  <span class="phone">+1 555 010 2040</span>
  <span class="divider"></span>
  <span class="account">Have an account? <a href="#">Register</a> of <a href="#">Sign In</a></span>
</header>

<nav class="abs navbar">
  <div class="brand">RPMH</div>
  <a class="nav-link" style="left:203px" href="#">How It Works?</a>
  <a class="nav-link" style="left:328px" href="#">Eligibility</a>
  <a class="nav-link" style="left:426px" href="#">Get Started</a>
  <a class="nav-link" style="left:555px" href="#">About</a>
  <a class="nav-link" style="left:632px" href="#">Blog</a>
  <div class="search">
    <span>Search the rules</span>
    <svg width="18" height="18" viewBox="0 0 18 18" fill="none" stroke="#999" stroke-width="1.3">
      <circle cx="10.5" cy="7.5" r="5.5"/><line x1="6.6" y1="11.4" x2="1.5" y2="16.5"/>
    </svg>
  </div>
</nav>

<section class="abs hero">
  <div class="hero-portrait" role="img" aria-label="Photo of a smiling small business owner in a white shirt in a bright office"></div>
  <h1 class="hero-title">CROWDFUNDING<br>FOR BUSINESSES</h1>
  <p class="hero-sub" style="top:204px">Many rules. One easy path.</p>
  <a class="cta" href="#">GET STARTED NOW
    <svg width="9" height="12" viewBox="0 0 9 12" fill="none" stroke="#fff" stroke-width="2.4"><polyline points="2,1 7,6 2,11"/></svg>
  </a>
</section>

<svg class="abs" style="left:114px;top:496px" width="36" height="36" viewBox="0 0 36 36" fill="none" stroke="#7fcd1e" stroke-width="2" stroke-linejoin="round">
  <polygon points="4,16 14,4 20,10 15,13 22,20 19,24 12,17 8,22"/>
  <line x1="18" y1="20" x2="32" y2="34"/>
</svg>
<h2 class="abs section-title" style="left:164px;top:493px">Eligibility</h2>

<div class="abs feature-photo" role="img" aria-label="Photo of a small business team reviewing answers at a laptop"></div>
<h3 class="abs feature-title">Can You Raise Money Online?</h3>
<p class="abs feature-body">Answer a short set of yes/no questions about your company, its prior fundraising and its registrations. We check them against the current rules and tell you if you qualify and what information you will need.</p>
<a class="abs feature-link" href="#">Start Questionnaire ›</a>

<div class="abs progress"><div class="fill"></div></div>
<span class="abs stat-label" style="left:610px">STEPS</span>
<span class="abs stat-label" style="left:709px">QUESTIONS</span>
<span class="abs stat-label" style="left:857px">MINUTES</span>
<span class="abs stat-value" style="left:610px">5</span>
<span class="abs stat-value" style="left:709px">45</span>
<span class="abs stat-value" style="left:857px">15</span>

<svg class="abs" style="left:113px;top:941px" width="36" height="35" viewBox="0 0 36 35" fill="none" stroke="#7fcd1e" stroke-width="2" stroke-linejoin="round">
  <polygon points="18,2 22.5,12.5 34,13.5 25,21 28,32.5 18,26.5 8,32.5 11,21 2,13.5 13.5,12.5"/>
</svg>
<h2 class="abs section-title" style="left:164px;top:937px">From the Blog</h2>

<div class="abs thumb" style="left:116px;background:linear-gradient(90deg,#e9d2b4,#c9a98c)" role="img" aria-label="Photo for a blog post"></div>
<div class="abs thumb" style="left:363px;background:linear-gradient(90deg,#6b4a2c,#2a2a2a)" role="img" aria-label="Photo for a blog post"></div>
<div class="abs thumb" style="left:611px;background:linear-gradient(90deg,#5a2f24,#b73a2e)" role="img" aria-label="Photo for a blog post"></div>
<div class="abs thumb" style="left:858px;background:linear-gradient(90deg,#efe6d6,#bda58c)" role="img" aria-label="Photo for a blog post"></div>

</body>
</html>
```